App Design Project

We had an tavrix/vemo app built (freelancer), without any real design applied. Currently just made up of plain buttons and text. No colors, images, etc.
App is about 20 total pages, and contains a login window, a main menu, and then several different options that pull data via web services from our back-end.
About the app:
The application will be used by physicians, who are in essence speakers who are speaking on behalf of pharmaceutical companies, to train doctors on the use of their products. They will use the app to get a list of their upcoming speaking engagements, calendars, access to slide presentations, and the ability for them to submit expense forms with pictures of receipts, etc.
We need the following things:
* An App Icon
* An Tavrix startup screen
* Two Vemo startup screens (one portrait and one landscape)
* Color schedme recommendations for the pages
* Page design recommendations: header/footer
The Tavrix and Vemo startup screens are screens displayed while the app is loading (splash screen). They are simply a large version of the app's logo (with differing dimensions) and maybe some extra detail as the space allows more. The Vemo and Tavrix screens can be identical, but please note the size. orientation and aspect ratio differences.
Objects possibilities...(pick any/none/anything else that is appropriate):
* Person behind a podium
* Someone speaking / presenting
* be creative
Styles we like:
This is for pharma, so medical might be appropriate
open to recommendations
Keep in mind that we are looking for page design recommendations as well. We could provide sample screens with text, and then are looking for recommendations on color, and general page design.
A successful designer may also win several other apps currently under consideration.

```html
<!DOCTYPE html>
<html lang="en">
<head>
<meta charset="utf-8">
<title>Speaker Resource Center</title>
<link rel="stylesheet" href="https://fonts.googleapis.com/css2?family=Josefin+Sans:wght@300;400;600&display=swap">
<style>
  :root {
    --bg-light: #f7f4ec;
    --bg-mid: #ece7db;
    --bg-edge: #e2dccd;
    --ink: #2a2a2a;
    --rule: #c9c3b6;
    --button-green: #b9e2bd;
    --button-green-edge: #a3d3a8;
    --button-text: #ffffff;
    --field-fill: rgba(255, 255, 255, 0.35);
    --field-edge: rgba(180, 172, 156, 0.45);
    --field-text: rgba(150, 142, 126, 0.55);
  }
  * { margin: 0; padding: 0; box-sizing: border-box; }
  html, body {
    width: 800px;
    height: 1200px;
    overflow: hidden;
  }
  body {
    position: relative;
    font-family: "Josefin Sans", sans-serif;
    background: radial-gradient(ellipse at 50% 40%, var(--bg-light) 0%, var(--bg-mid) 65%, var(--bg-edge) 100%);
  }
  .brand {
    position: absolute;
    left: 0;
    top: 330px;
    width: 800px;
    text-align: center;
    font-family: "Josefin Sans", sans-serif;
    font-weight: 300;
    font-size: 150px;
    letter-spacing: 6px;
    color: var(--ink);
  }
  .brand-rule {
    position: absolute;
    left: 100px;
    top: 728px;
    width: 620px;
    height: 2px;
    background: var(--rule);
  }
  .tagline {
    position: absolute;
    left: 0;
    top: 758px;
    width: 800px;
    text-align: center;
    font-weight: 400;
    font-size: 42px;
    font-variant: small-caps;
    letter-spacing: 5px;
    color: var(--ink);
  }
  .login-button {
    position: absolute;
    left: 330px;
    top: 900px;
    width: 140px;
    height: 84px;
    border-radius: 10px;
    border: 2px solid var(--button-green-edge);
    background: var(--button-green);
    color: var(--button-text);
    font-family: "Josefin Sans", sans-serif;
    font-size: 34px;
    font-weight: 400;
    display: flex;
    align-items: center;
    justify-content: center;
  }
  .field {
    position: absolute;
    top: 1045px;
    height: 92px;
    border-radius: 18px;
    border: 3px solid var(--field-edge);
    background: var(--field-fill);
    color: var(--field-text);
    font-size: 32px;
    display: flex;
    align-items: center;
    justify-content: center;
  }
  .field-username { left: -25px; width: 413px; }
  .field-password { left: 412px; width: 413px; }
</style>
</head>
<body>
  <div class="brand">Veltro</div>
  <div class="brand-rule"></div>
  <div class="tagline">Speaker Resource Center</div>
  <div class="login-button">Log In</div>
  <div class="field field-username">...Username...</div>
  <div class="field field-password">...Password...</div>
</body>
</html>
```